Velorix Flyer

PROJECT: Digital Flyer for VeloRix

Format
1920 × 1080 px (landscape, optimized for presentations and email)
Deliverables
• PDF
• PNG

About VeloRix
VeloRix is a Dutch B2B software company providing a unified CRM and customer journey platform. We help businesses manage the entire customer lifecycle — from first contact to loyal customer — by centralizing all touchpoints in one system.
What sets us apart:
Extreme ease of use. The system is self-guiding, shows only what's relevant per employee, and requires virtually no training. All channels (email, phone, chat, in-store) come together in one place with automatic task distribution. Built-in AI functions as a smart digital colleague that continuously learns.
Target audience:
Directors and sales managers at B2B companies with multiple customer contact channels.

Goal:
We want to create a flyer that sets us apart from other CRM platform providers. Our aim is to achieve this through simplicity and a professional appearance. The design should reflect our core value: ease of use. The recipient should feel compelled to engage with us — not overwhelmed by information, but intrigued by clarity. Less is more.

Required Text Elements
Headline:
"CRM that adapts to how you work"
Subline:
"Discover how VeloRix simplifies your sales process"
Call-to-action:
"See it in action — book a call"
Contact details:
• hello@velorix.nl
• 023-5718469
• velorix.com

Required Visual Elements
• VeloRix logo (attached)

Design Style
• Modern / Minimalist
• Professional / Business
• Tech / Futuristic
• Clean with plenty of whitespace

Tone of voice:
Clear, positive and customer-focused. Practical and accessible business style aimed at communicating concrete value for users.

Design inspiration — please review these websites:
• orbantal.com
• ravelo.app
• quendo.com
• tirameld.com
• gonwisp.com
What We DON'T Want
• Bold / In-your-face
• Dense / Compact
• Trendy / Experimental
• Childlike / Cheerful
• Playful / Cartoonish
• Busy / Chaotic
Colors
Use the color palette from velorix.com (blues, whites, clean professional tones).
[Exact hex codes used for element on the website:
#344054;
#1a1b1f;
#0254ac
#002249;
#e5edf7;
background-color: #fff; ]
Competitors (for context only — do NOT copy)
• brinvolt.nl
• kelmarin.com
• dortavecrm.com
• wexalunda.com
Budget
$150
Deadline
January 26, 2026

```html
<!DOCTYPE html>
<html lang="en">
<head>
<meta charset="utf-8">
<title>VeloRix Flyer</title>
<link rel="stylesheet" href="https://fonts.googleapis.com/css2?family=Inter:wght@300;400;500;700;800&display=swap">
<style>
  :root {
    --navy: #102459;
    --ink: #1a1b1f;
    --button: #2c5fc1;
    --icon: #2a8ad6;
    --paper: #f7f8fc;
    --mist: #e5edf7;
    --haze: #c9dcf4;
  }
  * { margin: 0; padding: 0; box-sizing: border-box; }
  html, body {
    width: 1200px;
    height: 675px;
    overflow: hidden;
    background: var(--paper);
  }
  .flyer {
    position: relative;
    width: 1200px;
    height: 675px;
    overflow: hidden;
    font-family: "Inter", Arial, sans-serif;
    background: linear-gradient(180deg, #ffffff 0%, var(--paper) 100%);
  }
  .hero-visual {
    position: absolute;
    left: 440px;
    top: 60px;
    width: 760px;
    height: 615px;
    background:
      radial-gradient(ellipse 45% 30% at 58% 55%, rgba(190, 213, 243, 0.75) 0%, rgba(220, 233, 249, 0.45) 55%, rgba(247, 248, 252, 0) 100%),
      radial-gradient(ellipse 60% 40% at 70% 75%, rgba(210, 226, 247, 0.6) 0%, rgba(247, 248, 252, 0) 100%);
  }
  .brand {
    position: absolute;
    left: 67px;
    top: 42px;
    display: flex;
    align-items: center;
    gap: 14px;
  }
  .brand-mark {
    width: 48px;
    height: 48px;
    border-radius: 50%;
    background: var(--navy);
  }
  .brand-name {
    font-size: 44px;
    font-weight: 700;
    color: var(--navy);
    letter-spacing: -0.5px;
  }
  .headline {
    position: absolute;
    left: 66px;
    top: 146px;
    font-size: 66px;
    line-height: 70px;
    font-weight: 700;
    color: var(--navy);
    letter-spacing: -1.2px;
  }
  .subline {
    position: absolute;
    left: 67px;
    top: 300px;
    font-size: 33px;
    line-height: 43px;
    font-weight: 300;
    color: var(--ink);
    letter-spacing: -0.4px;
  }
  .cta {
    position: absolute;
    left: 67px;
    top: 412px;
    width: 469px;
    height: 70px;
    border-radius: 9px;
    background: var(--button);
    color: #ffffff;
    font-size: 31px;
    font-weight: 400;
    display: flex;
    align-items: center;
    justify-content: center;
    letter-spacing: -0.2px;
  }
  .contact-list {
    position: absolute;
    left: 70px;
    top: 520px;
    list-style: none;
  }
  .contact-item {
    display: flex;
    align-items: center;
    height: 30px;
    margin-bottom: 1px;
    font-size: 18px;
    font-weight: 400;
    color: var(--ink);
  }
  .contact-item:last-child { margin-top: 3px; }
  .contact-icon {
    width: 28px;
    height: 28px;
    margin-right: 15px;
    flex: none;
  }
</style>
</head>
<body>
  <main class="flyer">
    <div class="hero-visual" role="img" aria-label="Soft blue light swoosh with a faint CRM dashboard interface"></div>

    <div class="brand">
      <span class="brand-mark"></span>
      <span class="brand-name">VeloRix</span>
    </div>

    <h1 class="headline">CRM that adapts<br>to how you work</h1>

    <p class="subline">Discover how VeloRix<br>simplifies your sales process</p>

    <div class="cta">See it in action — book a call</div>

    <ul class="contact-list">
      <li class="contact-item">
        <svg class="contact-icon" viewBox="0 0 28 28" aria-hidden="true">
          <rect x="1" y="6" width="26" height="17" fill="var(--icon)"/>
          <path d="M1 6 L14 16 L27 6 M1 23 L11 13.5 M27 23 L17 13.5" stroke="#ffffff" stroke-width="1.8" fill="none"/>
        </svg>
        hello@velorix.nl
      </li>
      <li class="contact-item">
        <svg class="contact-icon" viewBox="0 0 28 28" aria-hidden="true">
          <path d="M7 3 L11 8 L9 11.5 C10.5 15 13 17.5 16.5 19 L20 17 L25 21 L22 25 C13 24.5 4 15.5 3.5 6.5 Z" fill="var(--icon)"/>
        </svg>
        023-5718469
      </li>
      <li class="contact-item">
        <svg class="contact-icon" viewBox="0 0 28 28" aria-hidden="true">
          <g fill="none" stroke="var(--icon)" stroke-width="1.8">
            <circle cx="14" cy="14" r="12.5"/>
            <ellipse cx="14" cy="14" rx="5.5" ry="12.5"/>
            <line x1="14" y1="1.5" x2="14" y2="26.5"/>
            <line x1="1.5" y1="14" x2="26.5" y2="14"/>
            <path d="M3.5 8 H24.5 M3.5 20 H24.5"/>
          </g>
        </svg>
        velorix.com
      </li>
    </ul>
  </main>
</body>
</html>
```